Veltrano - Mechanic/Collision Center Business Card

We're looking for a business card design for our mechanic/ collision repair shop.

Can be with colours or monochromatic.

See the attached files.

Many thanks

```html
<!DOCTYPE html>
<html lang="pt">
<head>
<meta charset="utf-8">
<title>Veltrano – Business Card</title>
<link href="https://fonts.googleapis.com/css2?family=Arimo:wght@400;700&display=swap" rel="stylesheet">
<style>
  :root {
    --bg: #2a2a2b;
    --card-dark: #1b1e21;
    --card-light: #ffffff;
    --accent: #2a9ad9;
    --text-light: #d6d8da;
    --brand-dark: #1b1e21;
  }
  * { box-sizing: border-box; margin: 0; padding: 0; }
  html, body { width: 1200px; height: 895px; overflow: hidden; background: var(--bg); }
  body { position: relative; font-family: "Arimo", Arial, sans-serif; }

  .card {
    position: absolute;
    width: 560px; height: 320px;
    border-radius: 22px;
    overflow: hidden;
    box-shadow: 0 14px 30px rgba(0,0,0,.45);
  }
  .card--front { left: 60px; top: 70px; background: var(--card-dark); }
  .card--back  { left: 580px; top: 500px; background: var(--card-light); }

  .brand {
    position: absolute;
    display: flex; align-items: center; gap: 12px;
    font-weight: 700;
    letter-spacing: 1px;
    white-space: nowrap;
    line-height: 1;
  }
  .brand__dot { width: 22px; height: 22px; border-radius: 50%; flex: none; }
  .card--front .brand { left: 50%; top: 50%; transform: translate(-50%, -50%); font-size: 52px; color: #ffffff; }
  .card--front .brand__dot { background: #ffffff; }
  .card--back .brand { left: 50%; top: 48px; transform: translateX(-50%); font-size: 36px; color: var(--brand-dark); }
  .card--back .brand__dot { background: var(--accent); width: 18px; height: 18px; }

  .back-band { position: absolute; inset: 0; }

  .contacts {
    position: absolute; left: 36px; bottom: 20px;
    list-style: none;
    color: var(--text-light);
    font-size: 14px;
  }
  .contacts li { display: flex; align-items: center; gap: 10px; margin-top: 7px; }
  .contacts .icon {
    width: 20px; height: 20px; border-radius: 50%;
    background: var(--accent); border: 2px solid #ffffff;
    display: flex; align-items: center; justify-content: center;
  }
  .address {
    position: absolute; right: 30px; top: 150px;
    text-align: right;
    font-style: normal;
    color: var(--text-light);
    font-size: 14px;
    line-height: 1.75;
  }
</style>
</head>
<body>

<section class="card card--front" aria-label="Card front">
  <div class="brand"><span class="brand__dot"></span>VELTRANO</div>
</section>

<section class="card card--back" aria-label="Card back">
  <svg class="back-band" width="560" height="320" viewBox="0 0 560 320" aria-hidden="true">
    <polygon points="0,215 560,100 560,320 0,320" fill="var(--card-dark)"/>
    <line x1="0" y1="213" x2="560" y2="98" stroke="var(--accent)" stroke-width="5"/>
  </svg>

  <div class="brand"><span class="brand__dot"></span>VELTRANO</div>

  <address class="address">
    Veltrano, LDA<br>
    Rua das Oficinas, 42<br>
    Postal code: 1900-115 Lisboa
  </address>

  <ul class="contacts">
    <li>
      <span class="icon">
        <svg width="10" height="10" viewBox="0 0 24 24"><path fill="#fff" d="M6.6 10.8a15 15 0 0 0 6.6 6.6l2.2-2.2c.3-.3.7-.4 1-.2 1.1.4 2.3.6 3.6.6.6 0 1 .4 1 1V20c0 .6-.4 1-1 1A17 17 0 0 1 3 4c0-.6.4-1 1-1h3.5c.6 0 1 .4 1 1 0 1.3.2 2.5.6 3.6.1.3 0 .7-.2 1z"/></svg>
      </span>+351 214 550 382
    </li>
    <li>
      <span class="icon">
        <svg width="10" height="10" viewBox="0 0 24 24"><path fill="#fff" d="M2 5h20v14H2z"/><path d="M2 5l10 8 10-8" fill="none" stroke="#2a9ad9" stroke-width="2"/></svg>
      </span>veltrano.oficina@mail.pt
    </li>
    <li>
      <span class="icon"></span>www.veltrano-auto.pt
    </li>
  </ul>
</section>

</body>
</html>
```